International freight forwarder experienced in perishable handling needs a web design

We need a website designed that will allow us to capture more customers through the website. We would like a visually appealing design that is not so heavy on text. Our business covers the logistics and freight forwarding industries and we have offices in South America and the USA. Our main customers are importers USA, Europe, Asia and Russia and we currently work almost exclusively with perishable products such as fresh cut flowers, fresh exotics fruits, cacao, fresh fish etc. We would like to convey a fresh, modern approach to freight forwarding focusing on concepts such as - time sensitive, anytime-anywhere delivery, innovation, experience, reliability and confidence. Should include links with Chatterpost and Workvine. Our core solutions include: Core Services
*Air Freight
*Ocean Freight
*Warehousing & Distribution
Our industry solutions cover
*Flowers
*FMCG including, fruits, vegetables
*Live animals
*Automotive
*Consumer Goods
*Industrial
*Oil & Gas
*Pharma
* Event logistics
* Project logistics

Target Market(s)

Importers in Europe, USA, Asia, Middle East and Russia

Number of Pages Required

4 page

Font styles to use
Sans Serif

Colors
a1cd39
606060
000000

Requirements
Must have
• Photos of fresh cut flowers, FMCG such as cacao, fresh fish (packaged for shipping), fresh exotic fruits, pharma products (packaged for shipping), oil and gas etc. Internal customer login access
Nice to have
• Photos of cargo shipping carriers and cargo airline carriers. Features similar to those of following website http://www.vantoshipping.example/eng/main/index.jsp?FromURL=web
Should not have
• Too much text, needs to be visually pleasing

```html
<!DOCTYPE html>
<html lang="en">
<head>
<meta charset="utf-8">
<title>Corvane Freight</title>
<link href="https://fonts.googleapis.com/css2?family=Open+Sans:wght@300;400;600;700&family=Arimo:wght@400;700&display=swap" rel="stylesheet">
<style>
:root{
  --green:#6a9a14;
  --green-btn:#5f9410;
  --lime:#a1cd39;
  --text:#222;
  --grey:#606060;
  --muted:#8a8a8a;
  --footer-bg:#f2f2f2;
  --panel:rgba(60,60,60,.82);
}
*{margin:0;padding:0;box-sizing:border-box}
html,body{width:796px;height:1200px;overflow:hidden;background:#fff}
body{position:relative;font-family:"Open Sans",Arial,sans-serif;color:var(--text)}
.abs{position:absolute}
.hero-bg{left:0;top:0;width:796px;height:384px;background:linear-gradient(180deg,#5a4a36 0%,#2c2a2a 35%,#1d2230 70%,#2d3a4a 100%)}
.header{left:104px;top:57px;width:588px;height:45px;background:#fff}
.brand{left:14px;top:11px;display:flex;align-items:center;gap:6px;font-size:19px;color:#4a4a4a;font-weight:600;white-space:nowrap}
.brand i{display:block;width:14px;height:14px;border-radius:50%;background:var(--lime)}
.nav{left:0;top:0;width:100%;height:45px}
.nav a{position:absolute;top:19px;font-size:8.5px;font-weight:700;color:#444;text-decoration:none;white-space:nowrap}
.nav a.active{color:var(--green);font-size:9.5px;top:18px}
.slider{left:104px;top:102px;width:588px;height:246px;background:linear-gradient(160deg,#7f8a86 0%,#5d6b5e 40%,#9aa0a5 65%,#4a4d50 100%)}
.caption{left:10px;top:205px;font-size:12.5px;color:#fff;font-weight:300;white-space:nowrap}
.dots{left:9px;top:230px;display:flex;gap:2px}
.dots span{width:18px;height:5px;background:#ccc}
.dots span.on{background:var(--lime)}
.quote{left:414px;top:12px;width:162px;height:232px;background:var(--panel)}
.quote h2{position:absolute;left:5px;top:19px;font-size:13.5px;font-weight:300;color:#fff;white-space:nowrap}
.quote h2 b{font-weight:700}
.quote .field{position:absolute;left:5px;width:152px;height:17px;background:#fff;border-radius:2px;font-size:6px;color:#aaa;padding:4px 3px}
.quote .btn{position:absolute;left:5px;top:188px;width:58px;height:23px;background:var(--green-btn);color:#fff;font-size:9.5px;font-weight:700;text-align:center;line-height:23px;border-radius:2px}
.h-green{font-family:"Arimo",Arial,sans-serif;color:var(--green);font-weight:400}
.services-title{left:0;top:395px;width:796px;text-align:center;font-size:14.5px}
.card-img{width:185px;height:117px;top:422px}
.card-title{top:546px;font-size:11px;white-space:nowrap}
.card-body{top:564px;width:190px;font-size:8.2px;line-height:14.6px;color:#222}
.welcome-title{left:109px;top:645px;font-size:14.5px}
.welcome-img{left:110px;top:670px;width:330px;height:147px;background:linear-gradient(180deg,#e4e2d8 0%,#b6a690 50%,#8a5a48 100%)}
.welcome-body{left:110px;top:824px;width:332px;font-size:8.2px;line-height:14.6px;color:var(--muted);font-weight:300}
.news-title{left:453px;top:645px;font-size:14.5px}
.news-img{left:453px;width:85px;height:68px}
.news-head{left:545px;width:140px;font-size:11px;line-height:13.5px}
.news-body{left:545px;width:143px;font-size:8.2px;line-height:14.6px;color:#222;font-weight:300}
.footer{left:0;top:973px;width:796px;height:227px;background:var(--footer-bg)}
.f-head{top:29px;font-size:11px;font-weight:700;color:var(--green);font-family:"Arimo",Arial,sans-serif;white-space:nowrap}
.f-list{top:47px;list-style:none;font-size:8.4px;color:var(--grey);line-height:18.4px;font-weight:300}
.f-note{left:408px;top:44px;width:140px;font-size:8.4px;line-height:14.6px;color:var(--grey);font-weight:300}
.f-input{left:408px;width:135px;height:16px;background:#fff;border:1px solid #ddd;font-size:6px;color:#aaa;padding:4px 8px}
.f-btn{left:482px;top:125px;width:64px;height:16px;background:var(--green-btn);border-radius:8px;color:#fff;font-size:9.5px;font-weight:700;text-align:center;line-height:16px}
.soc-dot{left:603px;width:17px;height:17px;border-radius:50%;border:1px solid #d8d8d8;background:#fafafa}
.soc-label{right:105px;font-size:8.4px;color:var(--grey);text-align:right;font-weight:300}
.copy{left:0;top:1163px;width:796px;text-align:center;font-size:8px;color:#222}
</style>
</head>
<body>

<div class="abs hero-bg" role="img" aria-label="Night city skyline with illuminated skyscrapers"></div>

<header class="abs header">
  <div class="abs brand"><i></i>Corvane Freight</div>
  <nav class="abs nav">
    <a class="active" style="left:265px">Home</a>
    <a style="left:308px">About Us</a>
    <a style="left:363px">Services</a>
    <a style="left:415px">Login</a>
    <a style="left:457px">Testimonials</a>
    <a style="left:528px">Contact US</a>
  </nav>
</header>

<section class="abs slider" role="img" aria-label="Refrigerated freight truck carrying perishables on a highway">
  <p class="abs caption">Time-sensitive perishable freight, anytime &amp; anywhere</p>
  <div class="abs dots"><span class="on"></span><span></span><span></span><span></span></div>
  <form class="abs quote">
    <h2>Get A <b>Free Quote</b></h2>
    <div class="field" style="top:40px">Name</div>
    <div class="field" style="top:64px">E-Mail</div>
    <div class="field" style="top:91px">Company</div>
    <div class="field" style="top:116px">Phone</div>
    <div class="field" style="top:141px;height:41px">Message</div>
    <div class="btn">Submit</div>
  </form>
</section>

<h2 class="abs h-green services-title">Services</h2>

<div class="abs card-img" style="left:110px;background:linear-gradient(180deg,#1c2f6a 0%,#3a4f8a 50%,#7a7a80 100%)" role="img" aria-label="Cargo plane being loaded with fresh produce at dusk"></div>
<h3 class="abs h-green card-title" style="left:110px">Air Freight</h3>
<p class="abs card-body" style="left:110px">Cold-chain air cargo for fresh cut flowers, exotic fruits and fresh fish, flown from South America to importers in the USA, Europe and Asia.</p>

<div class="abs card-img" style="left:305px;background:linear-gradient(100deg,#2a3f8a 0%,#3a4fa0 45%,#e0a72a 65%,#f2b630 100%)" role="img" aria-label="Reefer containers being loaded onto a cargo ship"></div>
<h3 class="abs h-green card-title" style="left:305px">Ocean Freight</h3>
<p class="abs card-body" style="left:305px">Reefer container shipping for cacao, fruit and FMCG cargo, with full tracking and reliable sailings to Europe, Russia and the Middle East.</p>

<div class="abs card-img" style="left:502px;background:linear-gradient(180deg,#2a4fa0 0%,#1f3570 55%,#c58a3a 80%,#3a3020 100%)" role="img" aria-label="Temperature-controlled warehouse with packed perishables"></div>
<h3 class="abs h-green card-title" style="left:502px">Warehousing &amp; Distribution</h3>
<p class="abs card-body" style="left:502px">Temperature-controlled storage, packing and last-mile distribution, so perishable goods arrive fresh, on time and ready for market.</p>

<h2 class="abs h-green welcome-title">Welcome to Corvane Freight</h2>
<div class="abs welcome-img" role="img" aria-label="Cold storage warehouse aisle stacked with boxed flowers and fruit"></div>
<p class="abs welcome-body">Corvane Freight is an international freight forwarder specialised in perishable cargo. From our offices in South America and the USA we move fresh cut flowers, exotic fruits, cacao and fresh fish to importers across the USA, Europe, Asia, the Middle East and Russia. Every shipment is time sensitive, so we combine years of experience with modern cold-chain technology to deliver anytime, anywhere. Our industry solutions also cover FMCG, live animals, automotive, consumer goods, industrial, oil &amp; gas, pharma, event and project logistics, handled with the same reliability and care.</p>

<h2 class="abs h-green news-title">Latest news</h2>
<div class="abs news-img" style="top:670px;background:linear-gradient(180deg,#6a78a8 0%,#c88a6a 55%,#2a3048 100%)" role="img" aria-label="Fresh cut flowers boxed for air shipment"></div>
<h3 class="abs h-green news-head" style="top:668px">New cold-chain hub for fresh cut flowers</h3>
<p class="abs news-body" style="top:696px">Our new cold-chain hub shortens the time from farm to aircraft, keeping fresh cut flowers at the right temperature on every step of the way to Europe.</p>

<div class="abs news-img" style="top:798px;background:linear-gradient(180deg,#9ab8d8 0%,#c86a4a 55%,#2a4a6a 100%)" role="img" aria-label="Container ship loaded with reefer containers in port"></div>
<h3 class="abs h-green news-head" style="top:797px">Weekly reefer sailings to the Middle East</h3>
<p class="abs news-body" style="top:825px">Importers of exotic fruit and cacao can now book weekly reefer sailings with live temperature tracking and online access to every shipment document.</p>

<footer class="abs footer">
  <h4 class="abs f-head" style="left:113px">Quick Links</h4>
  <ul class="abs f-list" style="left:112px">
    <li>Home</li><li>About Us</li><li>Services</li><li>FAQs</li><li>Customer Login</li><li>Contact Us</li>
  </ul>
  <h4 class="abs f-head" style="left:257px">Support Links</h4>
  <ul class="abs f-list" style="left:259px">
    <li>Legal Notice</li><li>Privacy Policy</li><li>Terms &amp; Conditions</li><li>Help</li>
  </ul>
  <h4 class="abs f-head" style="left:408px">Newsletter Sign Up</h4>
  <p class="abs f-note">Sign-up for our daily emails by entering your information below:</p>
  <div class="abs f-input" style="top:77px">Name</div>
  <div class="abs f-input" style="top:103px">Enter Your E-Mail ID</div>
  <div class="abs f-btn">Subscribe</div>
  <h4 class="abs f-head" style="left:602px">Connect With Us</h4>
  <div class="abs soc-dot" style="top:45px"></div><span class="abs soc-label" style="top:49px">Chirpline</span>
  <div class="abs soc-dot" style="top:68px"></div><span class="abs soc-label" style="top:72px">Chatterpost</span>
  <div class="abs soc-dot" style="top:91px"></div><span class="abs soc-label" style="top:95px">Workvine</span>
</footer>
<p class="abs copy">© 2015 &nbsp;Corvane Freight Group.</p>

</body>
</html>
```